Package of web graphics needed

Utilizing a recently selected logo from a Loom Bazaar contest, we need to have some ads, fb cover, home page slide image created for our new 844-Toll-Free Number Product. Please feel free to check our site at www.marbleoakline.com

You'll find attached the 844 toll free logo in 2 layouts.

Here are the ads and dimensions of each that are needed:
1.)Banners/ads - 468x60
468×60 px
125×125 px
120×600 px
120x90 px
88×31 px button
5.)FB Cover - 851 x 315
6.)Home page slider image - 944 x 328

Here is the text & some ideas to use for these. Feel free to use different versions depending on which ad they work better on:
-

Market Your Business in a Memorable Way – Pre-Order Yours Today, Deadline: Dec. 7th
[include logo]
-
[844 logo] Don't Miss out on your chance to finally get a great vanity!

Order Yours Today
-

Don't Miss out on your chance to finally get a great vanity!
Dec. 7th Deadline to pre-order

Don't Ignore 844!– The newest toll free prefix – Coming Dec. 7th – Get Yours Today

FB COVER guidelines -
Requirements:
Include the logo
Limited Time Left – Get your Reservation in by December 7th

HOME PAGE Image Slide:
Use the logo,

Couple of Ideas we're interested in seeing:

[Billboard sign stock image … with the number 833-Grab-ONE on the billboard]
[844 logo and caricature] [1 caricature looking surprised]

Reason: Need more designs to review !

```html
<!DOCTYPE html>
<html lang="en">
<head>
<meta charset="utf-8">
<title>Dialcrest Lines – Web Ad Package</title>
<link href="https://fonts.googleapis.com/css2?family=Indie+Flower&family=Abril+Fatface&family=Tinos:wght@400;700&display=swap" rel="stylesheet">
<style>
  :root{
    --green-top:#4ba81c;
    --green-bottom:#0b8a00;
    --green-band:#118d06;
    --green-light:#3fa521;
    --navy:#063263;
    --sky-top:#2f7fd0;
    --sky-bottom:#cfe4f7;
    --red:#ff1c0a;
    --white:#ffffff;
  }
  html,body{margin:0;padding:0;width:1200px;height:1000px;overflow:hidden;background:var(--white);}
  .canvas{position:relative;width:1200px;height:1000px;font-family:"Tinos",serif;}
  .ad{position:absolute;overflow:hidden;}
  .ad > svg.bg{position:absolute;left:0;top:0;width:100%;height:100%;}
  .ad .txt{position:absolute;margin:0;}
  .hand{font-family:"Indie Flower",cursive;color:var(--white);line-height:1.1;letter-spacing:3px;}
  .cta{font-family:"Abril Fatface",serif;color:var(--red);text-shadow:0 0 3px #fff,0 0 6px rgba(255,255,255,.8);white-space:nowrap;letter-spacing:1px;}
  .serif-white{font-family:"Tinos",serif;color:var(--white);}
  .brand{font-family:"Tinos",serif;font-weight:700;color:var(--navy);line-height:1;}

  /* slider 944x328 */
  .slider{left:23px;top:13px;width:944px;height:328px;}
  .slider .brand{left:40px;top:95px;font-size:44px;width:280px;}
  .slider .hand{left:450px;top:42px;width:470px;font-size:35px;}
  .slider .cta{left:400px;top:182px;font-size:55px;}
  .slider .footer{left:14px;top:284px;font-size:33px;letter-spacing:1px;white-space:nowrap;}

  /* fb cover 851x350 */
  .cover{left:23px;top:610px;width:851px;height:350px;}
  .cover .brand{left:35px;top:70px;font-size:40px;width:260px;}
  .cover .hand{left:352px;top:12px;width:480px;font-size:34px;}
  .cover .cta{left:322px;top:135px;font-size:55px;}
  .cover .footer{left:8px;top:220px;font-size:31px;letter-spacing:1px;white-space:nowrap;}

  /* 125x125 */
  .square{left:1014px;top:130px;width:125px;height:125px;}
  .square .brand{left:0;top:10px;width:125px;text-align:center;font-size:14px;}
  .square .line{left:4px;top:58px;width:117px;text-align:center;font-size:8.5px;color:var(--white);line-height:1.15;}
  .square .cta{left:0;top:81px;width:125px;text-align:center;font-size:12px;letter-spacing:0;}
  .square .foot{left:3px;top:100px;width:119px;text-align:center;font-size:6.5px;color:var(--white);font-weight:700;line-height:1.2;}

  /* 468x60 */
  .leader{left:64px;top:475px;width:468px;height:60px;}
  .leader .brand{left:6px;top:10px;font-size:19px;white-space:nowrap;}
  .leader .line{left:210px;top:4px;width:258px;text-align:center;font-size:10px;color:var(--white);white-space:nowrap;}
  .leader .cta{left:210px;top:20px;width:258px;text-align:center;font-size:17px;letter-spacing:0;}
  .leader .foot{left:0;top:46px;width:468px;text-align:center;font-size:10px;color:var(--white);font-weight:700;white-space:nowrap;}

  /* 88x31 */
  .button{left:594px;top:490px;width:88px;height:31px;}
  .button .brand{left:22px;top:6px;width:44px;text-align:center;font-size:8px;}

  /* 120x90 */
  .small{left:737px;top:460px;width:120px;height:90px;}
  .small .brand{left:2px;top:12px;width:72px;text-align:center;font-size:12px;}
  .small .line{left:79px;top:3px;width:40px;text-align:center;font-size:5.5px;color:var(--white);font-weight:700;line-height:1.25;}
  .small .cta{left:0;top:58px;width:120px;text-align:center;font-size:10px;letter-spacing:0;}
  .small .foot{left:1px;top:72px;width:118px;text-align:center;font-size:5.5px;color:var(--white);font-weight:700;line-height:1.25;}

  /* 120x592 skyscrapers */
  .tower{width:120px;height:592px;}
  .tower-a{left:936px;top:378px;}
  .tower-b{left:1076px;top:383px;}
  .tower .brand{left:0;top:25px;width:120px;text-align:center;font-size:21px;}
  .tower .line{left:10px;top:115px;width:100px;text-align:center;font-size:15px;line-height:1.2;}
  .tower .cta{left:0;top:240px;width:120px;text-align:center;font-size:32px;line-height:1.25;white-space:normal;letter-spacing:0;}
  .tower .foot{left:6px;top:448px;width:108px;text-align:center;font-size:13px;color:var(--white);line-height:1.6;}
</style>
</head>
<body>
<div class="canvas">

  <!-- Home page slider -->
  <section class="ad slider">
    <svg class="bg" viewBox="0 0 944 328" preserveAspectRatio="none">
      <defs>
        <linearGradient id="gs" x1="0" y1="0" x2="0" y2="1"><stop offset="0" stop-color="#4ba81c"/><stop offset="1" stop-color="#0b8a00"/></linearGradient>
        <linearGradient id="sky1" x1="0" y1="0" x2="0" y2="1"><stop offset="0" stop-color="#2f7fd0"/><stop offset="1" stop-color="#cfe4f7"/></linearGradient>
      </defs>
      <rect width="944" height="266" fill="url(#gs)"/>
      <path d="M0 0H455C385 70 425 200 335 266H0Z" fill="url(#sky1)" role="img" aria-label="Photo of a blank billboard against a blue sky with clouds"/>
      <path d="M455 0H475C405 70 445 200 360 266H335C425 200 385 70 455 0Z" fill="#063263"/>
      <rect y="266" width="944" height="62" fill="#118d06"/>
    </svg>
    <p class="txt brand">Dialcrest Lines</p>
    <p class="txt hand">Don't Miss out on your chance to finally get a great vanity!</p>
    <p class="txt cta">Order Yours Today</p>
    <p class="txt serif-white footer">Limited Time Left – Get your Reservation in by December 7th</p>
  </section>

  <!-- 125 x 125 -->
  <section class="ad square">
    <svg class="bg" viewBox="0 0 125 125" preserveAspectRatio="none">
      <rect width="125" height="125" fill="url(#gs)"/>
      <path d="M0 0H125V20C112 52 80 56 62 56C40 56 10 50 0 20Z" fill="#ffffff"/>
      <rect y="97" width="125" height="28" fill="#063263"/>
    </svg>
    <p class="txt brand">Dialcrest Lines</p>
    <p class="txt line">Don't Miss out on your chance to finally get a great vanity!</p>
    <p class="txt cta">Order Yours Today</p>
    <p class="txt foot">Market Your Business in a Memorable Way – Pre-Order Yours Today, Deadline: Dec. 7th</p>
  </section>

  <!-- 468 x 60 -->
  <section class="ad leader">
    <svg class="bg" viewBox="0 0 468 60" preserveAspectRatio="none">
      <rect width="468" height="44" fill="#ffffff"/>
      <path d="M230 0H468V44H200C222 36 215 5 230 0Z" fill="url(#gs)"/>
      <rect y="44" width="468" height="16" fill="#063263"/>
    </svg>
    <p class="txt brand">Dialcrest Lines</p>
    <p class="txt line">Don't Miss out on your chance to finally get a great vanity!</p>
    <p class="txt cta">Order Yours Today</p>
    <p class="txt foot">Market Your Business in a Memorable Way – Pre-Order Yours Today, Deadline: Dec. 7th</p>
  </section>

  <!-- 88 x 31 -->
  <section class="ad button">
    <svg class="bg" viewBox="0 0 88 31" preserveAspectRatio="none">
      <rect width="88" height="31" fill="#ffffff"/>
      <rect width="20" height="31" fill="#063263"/>
      <rect x="70" width="18" height="31" fill="url(#gs)"/>
    </svg>
    <p class="txt brand">Dialcrest Lines</p>
  </section>

  <!-- 120 x 90 -->
  <section class="ad small">
    <svg class="bg" viewBox="0 0 120 90" preserveAspectRatio="none">
      <rect width="120" height="90" fill="url(#gs)"/>
      <path d="M0 0H77V32C77 48 62 56 36 56H0Z" fill="#ffffff"/>
      <rect y="70" width="120" height="20" fill="#063263"/>
    </svg>
    <p class="txt brand">Dialcrest Lines</p>
    <p class="txt line">Don't Miss out on your chance to finally get a great vanity!</p>
    <p class="txt cta">Order Yours Today</p>
    <p class="txt foot">Market Your Business in a Memorable Way – Pre-Order Yours Today, Deadline: Dec. 7th</p>
  </section>

  <!-- 120 x 600 skyscrapers -->
  <section class="ad tower tower-a">
    <svg class="bg" viewBox="0 0 120 592" preserveAspectRatio="none">
      <rect width="120" height="592" fill="url(#gs)"/>
      <path d="M0 0H120V70C105 90 60 95 0 95Z" fill="#ffffff"/>
      <path d="M0 460C30 450 70 425 120 412V592H0Z" fill="#063263"/>
    </svg>
    <p class="txt brand">Dialcrest Lines</p>
    <p class="txt serif-white line">Don't Miss out on your chance to finally get a great vanity!</p>
    <p class="txt cta">Order Yours Today</p>
    <p class="txt foot">Market Your Business in a Memorable Way – Pre-Order Yours Today, Deadline: Dec. 7th</p>
  </section>

  <section class="ad tower tower-b">
    <svg class="bg" viewBox="0 0 120 592" preserveAspectRatio="none">
      <rect width="120" height="592" fill="url(#gs)"/>
      <path d="M0 0H120V70C105 90 60 95 0 95Z" fill="#ffffff"/>
      <path d="M0 445C20 425 70 412 120 412V592H0Z" fill="#063263"/>
    </svg>
    <p class="txt brand">Dialcrest Lines</p>
    <p class="txt serif-white line">Don't Miss out on your chance to finally get a great vanity!</p>
    <p class="txt cta">Order Yours Today</p>
    <p class="txt foot">Market Your Business in a Memorable Way – Pre-Order Yours Today, Deadline: Dec. 7th</p>
  </section>

  <!-- Facebook cover -->
  <section class="ad cover">
    <svg class="bg" viewBox="0 0 851 350" preserveAspectRatio="none">
      <defs>
        <linearGradient id="sky2" x1="0" y1="0" x2="0" y2="1"><stop offset="0" stop-color="#2f7fd0"/><stop offset="1" stop-color="#cfe4f7"/></linearGradient>
      </defs>
      <rect width="851" height="201" fill="url(#gs)"/>
      <path d="M0 0H335C300 60 330 150 235 201H0Z" fill="url(#sky2)" role="img" aria-label="Photo of a blank billboard against a blue sky with clouds"/>
      <path d="M335 0H352C318 60 350 150 258 201H235C330 150 300 60 335 0Z" fill="#063263"/>
      <rect y="201" width="851" height="80" fill="#118d06"/>
      <rect y="281" width="851" height="12" fill="#3fa521"/>
      <rect y="293" width="851" height="57" fill="#063263"/>
    </svg>
    <p class="txt brand">Dialcrest Lines</p>
    <p class="txt hand">Don't Miss out on your chance to finally get a great vanity!</p>
    <p class="txt cta">Order Yours Today</p>
    <p class="txt serif-white footer">Limited Time Left – Get your Reservation in by December 7th</p>
  </section>

</div>
</body>
</html>
```